WebDesign | Financial Services Firm - Risk Mitigation

We are a professional services consulting firm that specializes in high net worth individuals over $25,000,000, executives C-suite and above, closely held businesses owners, family offices and highly compensated employees.

Our focus is on risk mitigation and tax efficient strategies. Our clients take their risk on themselves and have a proven track record generating wealth. Our directive is to preserve and protect the wealth they’ve already created.

Our company Harbor Crest Advisory is geared around five directives of asset protection:
1) Legal Structuring
2) Leverage & Financing
3) Risk Management - Asset Protection & Insurance, Trustee Work
4) Asset Management & Investing - Under www.tqlvalemark.com
5) Tax Efficient Strategies

Our Company Mark is a Pentagon with a key in the middle. A pentagon is the most efficient defensive structure. Each point of a pentagon is equal distance front every point . Each side provides support to another and works together, which is the key to our clients success.

Our key colors are blue, black and silver.

We ‘re located in the Pacific Northwest with bi coastal and international clients. We have fewer, higher net worth clients and provide exceptional customer service. We do not do social media.

We'll need the following pages:
-Front Landing Page.
Front page has to have link to hbportal.docuvaultix.com for logging into secure site.
- Contact & About Us Page
- Our Team Page
- Five Sides of Wealth Management
> Legal & Business Structuring
> Leverage & Financing
> Risk Management & Asset Protection.
> Asset Management and Investing - Will link to TQL (won't be turned on for a few months)
> Tax Efficient Strategies.

Industry/Entity Type

Financial Service

Coding

Coded - Design and coding required

Number of Pages Required

5+ page

Font styles to use
Sans Serif

Colors
0555a3

Requirements
Must have
• Our key colors are blue, black and silver.

-Front Landing Page.
- Contact & About Us Page
- Our Team Page
> Leverage & Financing
Nice to have
• I have attached images that have been purchased for use on the webpage. Us or not.

location page: 847 W Alder Ln, Suite 412, Lake Oswego, OR 97035
Should not have
• lots of color.

```html
<!DOCTYPE html>
<html lang="en">
<head>
<meta charset="utf-8">
<title>Harbor Crest Advisory</title>
<link rel="stylesheet" href="https://fonts.googleapis.com/css2?family=Gelasio:wght@400;500;700&family=Poppins:wght@400;500;600&display=swap">
<style>
:root{
  --blue:#0555a3;
  --navy:#06336b;
  --deep:#0b3f7c;
  --ink:#111111;
  --text:#5b5f66;
  --mist:#e8eef6;
  --white:#ffffff;
  --silver:#c9d2dc;
}
*{box-sizing:border-box;margin:0;padding:0}
html,body{width:1200px;height:3202px;overflow:hidden}
body{position:relative;background:var(--white);font-family:"Poppins",sans-serif;color:var(--text)}
.abs{position:absolute}

.topbar{left:0;top:0;width:1200px;height:37px;background:linear-gradient(90deg,#0a4f93,#073f7c);color:var(--white);font-size:12px;display:flex;align-items:center;justify-content:flex-end;padding-right:62px;gap:10px}
.nav{left:0;top:37px;width:1200px;height:60px;background:var(--white);box-shadow:0 1px 3px rgba(0,0,0,.08);z-index:3}
.brand{left:68px;top:14px;display:flex;align-items:center;gap:10px}
.brand-dot{width:34px;height:34px;border-radius:50%;background:var(--navy);flex:none}
.brand-name{font-family:"Gelasio",serif;font-size:22px;font-weight:500;color:var(--navy);letter-spacing:.5px}
.menu{left:620px;top:24px;display:flex;gap:26px;font-size:12.5px;color:#444}
.menu .active{color:var(--blue)}
.login{left:1005px;top:9px;width:135px;height:42px;border-radius:21px;background:var(--navy);color:var(--white);font-family:"Gelasio",serif;font-weight:700;font-size:15px;display:flex;align-items:center;padding-left:26px}
.btn-ring{position:absolute;right:4px;top:4px;width:34px;height:34px;border-radius:50%;background:var(--white);border:3px solid var(--navy)}

.hero{left:0;top:97px;width:1200px;height:699px;background:linear-gradient(100deg,#d8e2ea 0%,#9fb5c9 25%,#5d84ab 55%,#1d5d98 80%,#0d4f8d 100%);clip-path:polygon(0 0,1200px 0,1200px 699px,292px 615px,0 699px)}
.hero-grass{left:0;top:620px;width:1200px;height:176px;background:linear-gradient(180deg,rgba(120,140,90,0) 0%,rgba(110,130,80,.55) 100%);clip-path:polygon(0 0,1200px 0,1200px 176px,292px 92px,0 176px)}
.hero-title{left:62px;top:318px;width:640px;font-family:"Gelasio",serif;font-weight:700;font-size:47px;line-height:49px;color:var(--ink)}
.hero-title span{color:var(--navy)}
.cta{left:60px;top:495px;width:210px;height:40px;border-radius:20px;background:linear-gradient(90deg,var(--navy),var(--blue));color:var(--white);font-family:"Gelasio",serif;font-weight:700;font-size:13px;display:flex;align-items:center;padding-left:19px}
.cta .btn-ring{width:32px;height:32px}

.welcome{left:0;top:884px;width:1200px;text-align:center}
.welcome .kicker{font-family:"Gelasio",serif;font-size:18px;color:var(--ink)}
.welcome h2{font-family:"Gelasio",serif;font-weight:500;font-size:35px;color:var(--blue);margin-top:4px;letter-spacing:.5px}
.welcome p{width:570px;margin:8px auto 0;font-size:12.5px;line-height:19.5px}

.wealth{left:0;top:1119px;width:1200px;height:759px;background:linear-gradient(135deg,#1465a6,#0a5598 50%,#0d5da0);clip-path:polygon(0 0,855px 90px,1200px 0,1200px 759px,298px 684px,0 759px)}
.wealth-title{left:0;top:1245px;width:1200px;text-align:center;font-family:"Gelasio",serif;font-weight:500;font-size:33px;color:var(--white);letter-spacing:.5px}
.pillar{width:260px;text-align:center;color:var(--white);font-family:"Gelasio",serif;font-size:17.5px;line-height:22px}
.pillar svg{display:block;margin:0 auto 10px}

.team-title{left:0;top:1934px;width:1200px;text-align:center;font-family:"Gelasio",serif;font-weight:500;font-size:36px;color:var(--blue)}
.card{width:451px;height:225px;border:2px solid var(--navy);background:var(--white)}
.card .bar-r{position:absolute;right:-2px;top:-2px;width:9px;height:80px;background:var(--navy)}
.card .bar-l{position:absolute;left:-2px;bottom:-2px;width:9px;height:92px;background:var(--navy)}
.card h3{position:absolute;left:192px;top:18px;font-family:"Gelasio",serif;font-weight:500;font-size:18px;color:var(--ink)}
.card p{position:absolute;left:192px;top:58px;width:247px;font-size:12px;line-height:19.5px;color:var(--text)}
.card a{position:absolute;left:192px;top:181px;font-size:12px;color:var(--navy);text-decoration:underline;font-weight:500}
.portrait{position:absolute;left:14px;top:98px}

.contact-bg{left:0;top:2300px;width:1200px;height:560px;background:var(--mist);clip-path:polygon(0 0,855px 90px,1200px 0,1200px 560px,0 560px)}
.contact-title{left:0;top:2420px;width:1200px;text-align:center;font-family:"Gelasio",serif;font-weight:500;font-size:35px;color:var(--blue)}
.field{height:36px;background:var(--white);border:1px solid #dfe5ec;font-size:12px;color:#666;padding:9px 9px}
.field.focus{border:1.5px solid var(--navy)}
.submit{left:525px;top:2660px;width:150px;height:41px;border-radius:21px;background:var(--navy);color:var(--white);font-family:"Gelasio",serif;font-weight:700;font-size:13.5px;display:flex;align-items:center;padding-left:15px}

.footer{left:0;top:2744px;width:1200px;height:421px;background:var(--navy);clip-path:polygon(0 85px,249px 0,1200px 80px,1200px 421px,0 421px)}
.f-brand{left:62px;top:2868px;width:230px;display:flex;align-items:center;gap:10px}
.f-brand .brand-dot{background:var(--white);width:40px;height:40px}
.f-brand .brand-name{color:var(--white);font-size:19px;line-height:22px}
.f-about{left:62px;top:2935px;width:230px;font-size:12px;line-height:19.5px;color:var(--white)}
.f-col{top:2855px;color:var(--white)}
.f-col h4{font-family:"Gelasio",serif;font-weight:500;font-size:17.5px;margin-bottom:12px}
.f-col li{list-style:none;font-size:12px;line-height:30px}
.f-col li.wrap{padding-left:11px;text-indent:-11px;width:190px}
.f-contact{display:flex;gap:10px;font-size:12px;line-height:19px;margin-bottom:20px;width:230px}
.f-contact svg{flex:none}
.copyright{left:0;top:3165px;width:1200px;height:37px;background:var(--blue);color:var(--white);font-size:12px;text-align:center;line-height:37px}
</style>
</head>
<body>

<div class="abs topbar">
  <svg width="16" height="20" viewBox="0 0 16 20"><path d="M8 1a6 6 0 0 1 6 6c0 4.5-6 11-6 11S2 11.5 2 7a6 6 0 0 1 6-6z" fill="none" stroke="#fff" stroke-width="1.6"/><circle cx="8" cy="7" r="2.2" fill="none" stroke="#fff" stroke-width="1.6"/></svg>
  <span>847 W Alder Ln, Suite 412, Lake Oswego, OR 97035</span>
</div>

<header class="abs nav">
  <div class="abs brand"><span class="brand-dot"></span><span class="brand-name">HARBOR CREST ADVISORY</span></div>
  <nav class="abs menu"><span class="active">Home</span><span>About Us</span><span>Wealth Management</span><span>Contact Us</span></nav>
  <div class="abs login">LOGIN<span class="btn-ring"></span></div>
</header>

<section class="abs hero" role="img" aria-label="Photograph of a two-storey blue suburban house among bare trees under a pale sky"></section>
<div class="abs hero-grass" aria-hidden="true"></div>
<h1 class="abs hero-title">Real Estate Investors and Closely Held <span>Business Owners to protect</span></h1>
<div class="abs cta">FREE CONSULTATION<span class="btn-ring"></span></div>

<section class="abs welcome">
  <div class="kicker">Welcome To</div>
  <h2>HARBOR CREST ADVISORY</h2>
  <p>Lorem Ipsum is simply dummy text of the printing and typesetting industry. Lorem Ipsum has been the industry's standard dummy text ever since the 1500s, when an unknown printer took a galley of type and scrambled it to make a type specimen book.</p>
  <p>It has survived not only five centuries, but also the leap into electronic typesetting, remaining essentially unchanged. It was popularised in the 1960s with the release of Letraset sheets containing Lorem Ipsum passages,</p>
</section>

<section class="abs wealth" role="img" aria-label="Blue-toned photograph of stacked coins over banknotes"></section>
<h2 class="abs wealth-title">Wealth Management</h2>

<div class="abs pillar" style="left:68px;top:1318px">
  <svg width="144" height="140" viewBox="0 0 144 140"><polygon points="72,4 139,52 113,134 31,134 5,52" fill="none" stroke="#fff" stroke-width="5"/><polygon points="72,22 121,57 102,118 42,118 23,57" fill="rgba(255,255,255,.18)"/><circle cx="72" cy="66" r="22" fill="none" stroke="#fff" stroke-width="2"/><circle cx="72" cy="60" r="7" fill="none" stroke="#fff" stroke-width="2"/><path d="M60 80c2-9 22-9 24 0" fill="none" stroke="#fff" stroke-width="2"/></svg>
  Legal &amp; Business<br>Structuring
</div>
<div class="abs pillar" style="left:468px;top:1318px">
  <svg width="144" height="140" viewBox="0 0 144 140"><polygon points="72,4 139,52 113,134 31,134 5,52" fill="none" stroke="#fff" stroke-width="5"/><polygon points="72,22 121,57 102,118 42,118 23,57" fill="rgba(255,255,255,.18)"/><rect x="56" y="46" width="30" height="40" fill="none" stroke="#fff" stroke-width="2"/><path d="M62 56h18M62 64h18M62 72h12" stroke="#fff" stroke-width="2"/><path d="M92 50l-10 30" stroke="#fff" stroke-width="3"/></svg>
  Leverage &amp; Financing
</div>
<div class="abs pillar" style="left:870px;top:1318px">
  <svg width="144" height="140" viewBox="0 0 144 140"><polygon points="72,4 139,52 113,134 31,134 5,52" fill="none" stroke="#fff" stroke-width="5"/><polygon points="72,22 121,57 102,118 42,118 23,57" fill="rgba(255,255,255,.18)"/><path d="M72 44l9 15h-18z" fill="none" stroke="#fff" stroke-width="2"/><path d="M52 72l12-6 8 6 8-6 12 6-10 12H62z" fill="none" stroke="#fff" stroke-width="2"/></svg>
  Risk Management &amp; Asset<br>Protection
</div>
<div class="abs pillar" style="left:272px;top:1556px">
  <svg width="144" height="140" viewBox="0 0 144 140"><polygon points="72,4 139,52 113,134 31,134 5,52" fill="none" stroke="#fff" stroke-width="5"/><polygon points="72,22 121,57 102,118 42,118 23,57" fill="rgba(255,255,255,.18)"/><rect x="52" y="46" width="22" height="36" fill="none" stroke="#fff" stroke-width="2"/><rect x="74" y="58" width="18" height="24" fill="none" stroke="#fff" stroke-width="2"/><path d="M57 52h4M65 52h4M57 60h4M65 60h4M57 68h4M65 68h4M48 86h48" stroke="#fff" stroke-width="2"/></svg>
  Asset Management and<br>Investing
</div>
<div class="abs pillar" style="left:685px;top:1556px">
  <svg width="144" height="140" viewBox="0 0 144 140"><polygon points="72,4 139,52 113,134 31,134 5,52" fill="none" stroke="#fff" stroke-width="5"/><polygon points="72,22 121,57 102,118 42,118 23,57" fill="rgba(255,255,255,.18)"/><rect x="52" y="46" width="30" height="38" fill="none" stroke="#fff" stroke-width="2"/><circle cx="62" cy="56" r="5" fill="none" stroke="#fff" stroke-width="2"/><path d="M58 78v-6M64 78v-10M70 78v-4" stroke="#fff" stroke-width="2"/><rect x="78" y="64" width="14" height="20" fill="none" stroke="#fff" stroke-width="2"/></svg>
  Tax Efficient Strategies.
</div>

<h2 class="abs team-title">Our Team</h2>

<article class="abs card" style="left:127px;top:1996px">
  <span class="bar-r"></span><span class="bar-l"></span>
  <h3>Marcus Hollander</h3>
  <p>Marcus Hollander is the Financial Strategist and Founder who partners with C-Suite Executives, Family Offices, Real Estate Investors and Closely Held Business Owners to protect and maximize their wealth. After spending 15</p>
  <a>READ MORE</a>
  <svg class="portrait" width="158" height="152" viewBox="0 0 158 152" role="img" aria-label="Portrait photo of Marcus Hollander"><defs><linearGradient id="pa" x1="0" y1="0" x2="0" y2="1"><stop offset="0" stop-color="#7f9a6a"/><stop offset="1" stop-color="#2f3a4a"/></linearGradient></defs><polygon points="79,2 156,58 127,150 31,150 2,58" fill="url(#pa)" stroke="#06336b" stroke-width="2"/></svg>
</article>

<article class="abs card" style="left:622px;top:1996px">
  <span class="bar-r"></span><span class="bar-l"></span>
  <h3>Evan Radcliffe</h3>
  <p>Evan Radcliffe is the CFO and Strategist for our closely held businesses. As a former CPA, he takes in-depth roles in closely held companies as a financial consultant during times of exit or transition.</p>
  <a>READ MORE</a>
  <svg class="portrait" width="158" height="152" viewBox="0 0 158 152" role="img" aria-label="Portrait photo of Evan Radcliffe"><defs><linearGradient id="pb" x1="0" y1="0" x2="0" y2="1"><stop offset="0" stop-color="#8a8478"/><stop offset="1" stop-color="#3b49c9"/></linearGradient></defs><polygon points="79,2 156,58 127,150 31,150 2,58" fill="url(#pb)" stroke="#06336b" stroke-width="2"/></svg>
</article>

<section class="abs contact-bg"></section>
<h2 class="abs contact-title">Contact Us</h2>
<div class="abs field focus" style="left:232px;top:2480px;width:363px">Name*</div>
<div class="abs field" style="left:603px;top:2480px;width:363px">Email*</div>
<div class="abs field" style="left:232px;top:2528px;width:363px">Phone no*</div>
<div class="abs field" style="left:603px;top:2528px;width:363px">Details your request*</div>
<div class="abs field" style="left:232px;top:2576px;width:736px;height:74px">Message</div>
<div class="abs submit">SUBMIT NOW<span class="btn-ring" style="width:33px;height:33px"></span></div>

<footer class="abs footer"></footer>
<div class="abs f-brand"><span class="brand-dot"></span><span class="brand-name">HARBOR CREST<br>ADVISORY</span></div>
<p class="abs f-about">As a Key Executive, Evan Radcliffe, is noted for integrating new financial delivery strategies and restructuring and streamlining operations.</p>

<div class="abs f-col" style="left:338px">
  <h4>Quick Links</h4>
  <ul><li>- Home</li><li>- About Us</li><li>- Wealth Management</li><li>- Contact Us</li><li>- Login</li></ul>
</div>
<div class="abs f-col" style="left:613px">
  <h4>Wealth Management</h4>
  <ul><li>- Legal &amp; Business Structuring</li><li>- Leverage &amp; Financing</li><li class="wrap">- Risk Management &amp; Asset Protection</li><li class="wrap">- Asset Management and Investing</li><li>- Tax Efficient Strategies</li></ul>
</div>
<div class="abs f-col" style="left:888px">
  <h4>Contact Us</h4>
  <div class="f-contact"><svg width="16" height="20" viewBox="0 0 16 20"><path d="M8 1a6 6 0 0 1 6 6c0 4.5-6 11-6 11S2 11.5 2 7a6 6 0 0 1 6-6z" fill="none" stroke="#fff" stroke-width="1.6"/><circle cx="8" cy="7" r="2.2" fill="none" stroke="#fff" stroke-width="1.6"/></svg><span>847 W Alder Ln, Suite 412, Lake Oswego, OR 97035</span></div>
  <div class="f-contact"><svg width="18" height="14" viewBox="0 0 18 14"><rect x="1" y="1" width="16" height="12" fill="none" stroke="#fff" stroke-width="1.5"/><path d="M1 1l8 7 8-7" fill="none" stroke="#fff" stroke-width="1.5"/></svg><span>info@harborcrestadvisory.com</span></div>
  <div class="f-contact"><svg width="18" height="18" viewBox="0 0 18 18"><path d="M4 1l3 4-2 2c1 2 3 4 5 5l2-2 4 3-2 3C8 16 2 10 1 4z" fill="#fff"/></svg><span>123 456 7890</span></div>
</div>

<div class="abs copyright">©2021 HARBOR CREST ADVISORY-All Right Reserves</div>

</body>
</html>
```